Wellness Coach needs a Business Card

I need a business card for a start-up coaching business called Brightfern Vitality Partners. I don't have a logo as such but I am looking to have a web page created in a few months time and hopefully the person who designs this card will be able to do or help with the web project. This business card will be used primarily for networking and for initial clients.

As the name implies, the coaching focus is wide-ranging and includes multiple facets of health and wellness, including physical, mental, spiritual, etc. I am a Personal Trainer so the main focus will be physical training, but with the other areas of life / wellness included.

My information for the card:

Dorian Pleshey
Director
Brightfern Vitality Partners

Phone: 0413 862051
Address: PO Box 514 Mitchell ACT 2911
email: dorian@brightfernvitalitypartners.com.au
web: http://www.brightfernvitalitypartners.com.au

Target Market(s)

People wanting to change their life by getting fit and by addressing issues in their lives that are holding them back. I will target people already into fitness but who want to extend their approach into life coaching.

Industry/Entity Type

Health

Requirements
Must have
• - I am keen on a single sided business card design but if your design lends itself to a double sided design then I'm open to that thanks.

- I love the idea of fresh - something that represents the awakening of somebody who has been dormant. Lime green strikes me as fresh, but this is just an idea, not mandatory.
Nice to have
• - I'm keen for minimisation but I don't mind an image in the background taking up the whole space, as long as it is not too busy.

- Two types of images that I can visualise are a mountain summit or a path leading into nature or up a mountain - an adventure! Again, not mandatory, just an idea.
Should not have
• - I'm not keen on over-crowding.
- One image I'm not keen on is someone standing on top of a mountain with their arms in the air - too cliché.

```html
<!DOCTYPE html>
<html lang="en">
<head>
<meta charset="utf-8">
<title>Brightfern Vitality Partners – Business Card</title>
<link rel="stylesheet" href="https://fonts.googleapis.com/css2?family=Oswald:wght@600&family=Open+Sans:wght@400;600&display=swap">
<style>
  :root {
    --sky: #0aaeea;
    --paper: #ffffff;
    --ink: #2b2f33;
    --contact-ink: #15303f;
    --backdrop: #e9ebee;
  }
  * { box-sizing: border-box; margin: 0; padding: 0; }
  html, body {
    width: 1200px; height: 1019px; overflow: hidden;
    background: var(--backdrop);
  }
  .sheet {
    width: 1200px; height: 1019px;
    display: flex; flex-direction: column;
    align-items: center; justify-content: center; gap: 56px;
  }
  .card {
    width: 720px; height: 412px;
    box-shadow: 0 6px 18px rgba(0,0,0,0.14);
  }

  /* Front: blue frame, white field */
  .card-front {
    background: var(--sky);
    padding: 40px;
  }
  .card-front .field {
    width: 100%; height: 100%;
    background: var(--paper);
    display: flex; align-items: center; justify-content: space-between;
    padding: 0 48px 0 44px;
  }
  .brand-name {
    font-family: "Open Sans", sans-serif;
    font-weight: 600;
    font-size: 19px;
    color: var(--sky);
    margin-top: -30px;
  }
  .person-name {
    font-family: "Oswald", sans-serif; font-weight: 600;
    font-size: 30px; color: var(--ink);
    text-transform: uppercase; letter-spacing: 1px;
    margin-top: 60px;
  }

  /* Back: white frame, blue field */
  .card-back {
    background: var(--paper);
    padding: 40px;
  }
  .card-back .field {
    width: 100%; height: 100%;
    background: var(--sky);
    display: flex; align-items: center;
    padding: 0 56px;
  }
  .contact-list { list-style: none; display: flex; flex-direction: column; gap: 14px; }
  .contact-item {
    display: flex; align-items: center; gap: 14px;
    font-family: "Open Sans", sans-serif; font-size: 16px;
    color: var(--contact-ink);
  }
  .contact-item.address { align-items: flex-start; margin-bottom: 10px; }
  .contact-icon { width: 18px; height: 18px; flex: none; fill: var(--contact-ink); }
</style>
</head>
<body>
<main class="sheet">

  <section class="card card-front" aria-label="Business card front">
    <div class="field">
      <p class="brand-name">Brightfern Vitality Partners</p>
      <p class="person-name">Dorian Pleshey</p>
    </div>
  </section>

  <section class="card card-back" aria-label="Business card back">
    <div class="field">
      <ul class="contact-list">
        <li class="contact-item address">
          <svg class="contact-icon" viewBox="0 0 24 24" aria-hidden="true"><path d="M12 2a7 7 0 0 0-7 7c0 5 7 13 7 13s7-8 7-13a7 7 0 0 0-7-7zm0 9.5A2.5 2.5 0 1 1 12 6.5a2.5 2.5 0 0 1 0 5z"/></svg>
          <span>PO Box 514<br>Mitchell ACT 2911</span>
        </li>
        <li class="contact-item">
          <svg class="contact-icon" viewBox="0 0 24 24" aria-hidden="true"><path d="M6.6 10.8a15.1 15.1 0 0 0 6.6 6.6l2.2-2.2a1 1 0 0 1 1-.25 11.4 11.4 0 0 0 3.6.57 1 1 0 0 1 1 1V20a1 1 0 0 1-1 1A17 17 0 0 1 3 4a1 1 0 0 1 1-1h3.5a1 1 0 0 1 1 1c0 1.25.2 2.45.57 3.57a1 1 0 0 1-.25 1z"/></svg>
          <span>0413 862051</span>
        </li>
        <li class="contact-item">
          <svg class="contact-icon" viewBox="0 0 24 24" aria-hidden="true"><path d="M7 1h10a2 2 0 0 1 2 2v18a2 2 0 0 1-2 2H7a2 2 0 0 1-2-2V3a2 2 0 0 1 2-2zm0 4v13h10V5zm5 14.5a1 1 0 1 0 0 2 1 1 0 0 0 0-2z"/></svg>
          <span>02 6117 4830</span>
        </li>
        <li class="contact-item">
          <svg class="contact-icon" viewBox="0 0 24 24" aria-hidden="true"><path d="M2 5h20v14H2zm2 2v.5l8 5 8-5V7zm0 2.8V17h16V9.8l-8 5z"/></svg>
          <span>dorian@brightfernvitalitypartners.com.au</span>
        </li>
        <li class="contact-item">
          <svg class="contact-icon" viewBox="0 0 24 24" aria-hidden="true"><path d="M12 2a10 10 0 1 0 0 20 10 10 0 0 0 0-20zm6.9 6h-3a15 15 0 0 0-1.3-3.9A8 8 0 0 1 18.9 8zM12 4c.9 1.2 1.6 2.6 2 4h-4c.4-1.4 1.1-2.8 2-4zM4.3 14a8 8 0 0 1 0-4h3.4a16 16 0 0 0 0 4zm.8 2h3a15 15 0 0 0 1.3 3.9A8 8 0 0 1 5.1 16zm3-8h-3a8 8 0 0 1 4.3-3.9A15 15 0 0 0 8.1 8zM12 20c-.9-1.2-1.6-2.6-2-4h4c-.4 1.4-1.1 2.8-2 4zm2.3-6H9.7a14 14 0 0 1 0-4h4.6a14 14 0 0 1 0 4zm.3 5.9a15 15 0 0 0 1.3-3.9h3a8 8 0 0 1-4.3 3.9zm1.7-5.9a16 16 0 0 0 0-4h3.4a8 8 0 0 1 0 4z"/></svg>
          <span>http://www.brightfernvitalitypartners.com.au</span>
        </li>
      </ul>
    </div>
  </section>

</main>
</body>
</html>
```